Healthy Snack/Confectionery Bar Logo & front of pack

KOVA LUMEN LOGO and ON PACK
Directionally, use of colours specified in the brief is important as consumers associate the brand values we want with these colours. Blue. Green Cyan on White background should probably be the base colours. Gradients and Swirls of Colour would be good, but welcome alternatives. Product imagery should be in a set window that works well with the logo design.

Core Target Audience: Adults seeking to reduce/avoid sugar due to health concerns (pre-diabetic/diabetic/sugar avoiders), Secondary Audiences: Healthcare professionals looking for strategies to reduce sugar consumption, Mothers seeking to reduce family sugar consumption. Core Design Objectives: “HEALTHY AND PREMIUM” “FRESH” / Tasty / Appetising (product illustration) / Premium, Natural and Low in Sugar (colour cues) / Expert / Effective / Recommended (endorsements and back of pack).
Cyan/Blue often used to denote No added Sugar. Cyan = R 0 G 255 B 255
Blue/Green often used to denote medical benefit. Blue= R 0 G 129 B 129 / Green= R 132 G 173 B 0
Kova Lumen Yellow – R 254 G 244 B 0 links to QRB Brand.
* RGB Values for Cyan and Blue and Green are for Guidance only.

Text & Fonts: No more than 6 words. Largest - KOVA LUMEN (SUGAR to be subservient / more in the background - LUMEN should stand out as the main word. Medium - PELLOW DRIFT - Medium & integrated into design - LOW SUGAR
Fonts Decorative – e.g. MICROBREW, PHOPSPHATE, CAMPUS, INTRO RUST, BURFORD RUSTIC (see glyphhaven.net)

Target Market(s)

UK / NORTHERN EUROPE / AFLLUENT

Font styles to use
Sans Serif
Decorative

Colors
ffffff
0455a3
add136
fbee3d
000000
34a7d8

Requirements
Must have
• The design is for a healthy snack bar logo. Ideally the files submitted should include the image in an on-pack situation (e.g. a cereal bar, flapjack or cookie)
Nice to have
• See brief.

```html
<!DOCTYPE html>
<html lang="en">
<head>
<meta charset="utf-8">
<title>Kova Lumen – Front of Pack</title>
<link rel="stylesheet" href="https://fonts.googleapis.com/css2?family=Fredoka:wght@700&family=Oswald:wght@600;700&display=swap">
<style>
  :root {
    --page-bg: #e9e9e9;
    --brand-blue: #0a6fd0;
    --brand-cyan: #18eef0;
    --brand-navy: #062b73;
    --brand-yellow: #fff200;
    --brand-gold: #d8b417;
    --white: #ffffff;
    --cocoa-light: #9a6650;
    --cocoa-dark: #4a2517;
  }
  html, body {
    margin: 0;
    width: 1200px;
    height: 1200px;
    overflow: hidden;
    background: var(--page-bg);
  }
  .canvas {
    position: relative;
    width: 1200px;
    height: 1200px;
    display: flex;
    align-items: center;
    justify-content: center;
  }
  .pack-front {
    width: 1000px;
    height: 400px;
    display: block;
    box-shadow: 0 18px 40px rgba(0,0,0,0.18);
  }
  .brand-name {
    font-family: "Fredoka", sans-serif;
    font-weight: 700;
    font-size: 92px;
    fill: var(--white);
    letter-spacing: 2px;
  }
  .product-name {
    font-family: "Oswald", sans-serif;
    font-weight: 700;
    font-size: 46px;
    fill: var(--brand-cyan);
    stroke: var(--brand-navy);
    stroke-width: 5px;
    paint-order: stroke fill;
    stroke-linejoin: round;
  }
  .claim-text {
    font-family: "Oswald", sans-serif;
    font-weight: 600;
    font-size: 34px;
    fill: var(--brand-navy);
    letter-spacing: 1px;
  }
</style>
</head>
<body>
<main class="canvas">
  <svg class="pack-front" viewBox="0 0 1000 400" xmlns="http://www.w3.org/2000/svg">
    <defs>
      <linearGradient id="sky-gradient" x1="0" y1="0" x2="1" y2="0">
        <stop offset="0" stop-color="var(--brand-blue)"/>
        <stop offset="0.55" stop-color="#12b7e8"/>
        <stop offset="1" stop-color="var(--brand-cyan)"/>
      </linearGradient>
      <linearGradient id="sun-gradient" x1="0" y1="0" x2="0" y2="1">
        <stop offset="0" stop-color="var(--brand-yellow)"/>
        <stop offset="0.7" stop-color="#f6dc0a"/>
        <stop offset="1" stop-color="var(--brand-gold)"/>
      </linearGradient>
      <linearGradient id="cocoa-gradient" x1="0" y1="0" x2="1" y2="1">
        <stop offset="0" stop-color="var(--cocoa-light)"/>
        <stop offset="1" stop-color="var(--cocoa-dark)"/>
      </linearGradient>
    </defs>

    <rect class="pack-sky" width="1000" height="400" fill="url(#sky-gradient)"/>

    <path class="pack-swoosh-edge" d="M0 322 Q 420 150 1000 118 L1000 400 L0 400 Z" fill="var(--white)"/>
    <path class="pack-swoosh" d="M0 334 Q 420 165 1000 131 L1000 400 L0 400 Z" fill="url(#sun-gradient)"/>

    <rect class="pack-gloss" x="0" y="18" width="1000" height="10" fill="var(--white)" opacity="0.45"/>
    <rect class="pack-gloss" x="0" y="372" width="1000" height="6" fill="var(--white)" opacity="0.4"/>

    <g class="product-window" role="img" aria-label="Photo of a milk chocolate bar broken into squares">
      <polygon points="612,218 690,196 1000,200 1000,400 770,400 742,380" fill="url(#cocoa-gradient)"/>
    </g>

    <text class="brand-name" x="140" y="125">KOVA LUMEN</text>

    <text class="product-name" x="255" y="285" textLength="300" lengthAdjust="spacingAndGlyphs">CHOCOLATE BAR</text>

    <g class="low-sugar-claim">
      <circle cx="272" cy="331" r="12" fill="var(--brand-navy)"/>
      <text class="claim-text" x="296" y="344">LOW SUGAR</text>
    </g>
  </svg>
</main>
</body>
</html>
```